Desk Allies Business Card

Contact Information for Business Card

Janne Voutilainen
Managing Director

3/47 Brindle Street Calder ACT 2918

Tel: +61 02 6257 3140
Mob: +61 0427 315 846

Email: janne@deskallies.com.au
Web: www.deskallies.com.au

Colors

Designer to choose colors to be used in the design.

Requirements
Must have
• Logo, Name, Title, Address, Telephone, Mobile, Email Address and Website
• "Desk Ally International Pty Ltd"

```html
<!DOCTYPE html>
<html lang="en">
<head>
<meta charset="utf-8">
<title>Desk Allies Business Card</title>
<link href="https://fonts.googleapis.com/css2?family=Lato:wght@400;700&family=Montserrat:wght@600&display=swap" rel="stylesheet">
<style>
  :root {
    --stage: #676767;
    --paper: #ffffff;
    --ink: #2b2b2b;
    --brand-blue: #1a6fc0;
    --muted: #7a7a7a;
    --rule: #a9a9a9;
    --back-dark: #333234;
  }
  * { margin: 0; padding: 0; box-sizing: border-box; }
  html, body { width: 1200px; height: 802px; overflow: hidden; }
  body { background: var(--stage); position: relative; font-family: "Lato", sans-serif; color: var(--ink); }

  .card { position: absolute; top: 274px; width: 442px; height: 265px; }
  .card-front { left: 136px; background: var(--paper); }
  .card-back { left: 624px; background: var(--back-dark); }

  .brand { position: absolute; right: 32px; top: 56px; text-align: right; }
  .brand-line { display: flex; align-items: center; justify-content: flex-end; gap: 8px; }
  .brand-dot { width: 30px; height: 30px; border-radius: 50%; background: var(--brand-blue); }
  .brand-name { font-family: "Lato", sans-serif; font-weight: 700; font-size: 21px; color: var(--brand-blue); letter-spacing: 0.3px; }
  .brand-tagline { font-size: 7.5px; letter-spacing: 1.9px; color: var(--muted); text-transform: uppercase; margin-top: 1px; }

  .person { position: absolute; left: 23px; top: 132px; }
  .person-name { font-size: 17px; color: var(--brand-blue); letter-spacing: 0.4px; text-transform: uppercase; line-height: 1.1; }
  .person-title { font-size: 13px; line-height: 1.3; }

  .divider { position: absolute; left: 23px; right: 31px; top: 172px; height: 1px; background: var(--rule); }

  .contacts { position: absolute; left: 23px; top: 182px; list-style: none; font-size: 12.5px; line-height: 15.8px; }
  .contacts li { display: flex; align-items: center; gap: 6px; }
  .contacts svg { width: 10px; height: 10px; fill: var(--brand-blue); flex: none; }
  .contacts .icon-mail { fill: none; stroke: var(--brand-blue); stroke-width: 1.3; }

  .company { position: absolute; right: 31px; top: 184px; text-align: right; }
  .company-name { font-family: "Montserrat", sans-serif; font-weight: 600; font-size: 11px; color: var(--brand-blue); line-height: 14px; text-transform: uppercase; }
  .company-address { font-size: 12.5px; line-height: 15.8px; margin-top: 1px; }

  .back-pattern { position: absolute; inset: 0; background: var(--back-dark); }
  .back-brand { position: absolute; right: 48px; top: 112px; display: flex; align-items: center; gap: 8px; }
  .back-brand .brand-dot { width: 26px; height: 26px; }
  .back-brand .brand-name { font-size: 18px; }
</style>
</head>
<body>
  <section class="card card-front" aria-label="Business card front">
    <div class="brand">
      <div class="brand-line">
        <span class="brand-dot"></span>
        <span class="brand-name">DESK ALLIES</span>
      </div>
      <div class="brand-tagline">Ergonomic Office Environments</div>
    </div>

    <div class="person">
      <div class="person-name">Janne Voutilainen</div>
      <div class="person-title">Managing Director</div>
    </div>

    <div class="divider"></div>

    <ul class="contacts">
      <li><svg viewBox="0 0 10 10"><path d="M1 4c0-2 8-2 8 0v1H7V4H3v1H1z M2 5h6l1 4H1z"/></svg>+61 02 6257 3140</li>
      <li><svg viewBox="0 0 10 10"><path d="M3 0h4a1 1 0 0 1 1 1v8a1 1 0 0 1-1 1H3a1 1 0 0 1-1-1V1a1 1 0 0 1 1-1zm0 1.5v6h4v-6z"/></svg>+61 0427 315 846</li>
      <li><svg class="icon-mail" viewBox="0 0 10 10"><rect x="0.7" y="2.2" width="8.6" height="5.6"/><path d="M0.7 2.2L5 5.6L9.3 2.2"/></svg>janne@deskallies.com.au</li>
      <li><svg viewBox="0 0 10 10"><circle cx="5" cy="5" r="4.5"/></svg>www.deskallies.com.au</li>
    </ul>

    <div class="company">
      <div class="company-name">Desk Ally<br>International Pty Ltd</div>
      <div class="company-address">3/47 Brindle Street<br>Calder ACT 2918</div>
    </div>
  </section>

  <section class="card card-back" aria-label="Business card back">
    <div class="back-pattern" role="img" aria-label="Repeating tone-on-tone brand symbol pattern on dark charcoal"></div>
    <div class="back-brand">
      <span class="brand-dot"></span>
      <span class="brand-name">DESK ALLIES</span>
    </div>
  </section>
</body>
</html>
```